"BREAKING NEWS!" Fitness photos needed

Hello.... We are creating our new ads for Pellumra and Quorvidel and we need some photos manipulated and text added.

We have 5 photos total that we would like to have the Headline read "Breaking News" and we'll be split testing two different quotes, so I'd like to have:

AD #1:
Breaking News - Finally! Ridgecrest Gets the Gym That Actually Delivers Results (and It's Fun!)

And then a second set on the same photos that read:

AD #2:
Breaking News - Ridgecrest Residents Ditch Boring Workouts for This Life-Changing Fitness Experience

I'd like the photos to pop and stand out, so if color corrections need to be done, please feel free.

I've attached all photos and an example photo that DOES NOT need to be the same. It's just an example I saw that caught my eye, but I feel could be done better.

Thank you!

```html
<!DOCTYPE html>
<html lang="en">
<head>
<meta charset="utf-8">
<title>Breaking News Fitness Ads</title>
<link rel="stylesheet" href="https://fonts.googleapis.com/css2?family=Oswald:wght@700&family=Poppins:wght@600&display=swap">
<style>
  :root {
    --stage: #151515;
    --news-red: #f20a0a;
    --band-blue: #2a0cff;
    --band-violet: #7a22ea;
    --panel-white: #ffffff;
    --ink: #111111;
    --glow: #6cc0ff;
    --slice1-top: #c4bab2; --slice1-low: #5f5b50;
    --slice2-top: #e2a9bb; --slice2-low: #4a2a56;
    --slice3-top: #8a8aa0; --slice3-low: #33264f;
    --slice4-top: #d2b68e; --slice4-low: #7a2450;
    --slice5-top: #9aa0ae; --slice5-low: #272c3c;
  }
  html, body {
    margin: 0;
    padding: 0;
    width: 1200px;
    height: 979px;
    overflow: hidden;
    background: var(--stage);
  }
  .ad-set {
    display: flex;
    justify-content: center;
    align-items: center;
    gap: 40px;
    width: 1200px;
    height: 979px;
  }
  .ad-post {
    width: 560px;
    height: 560px;
    display: block;
  }
  .headline {
    font-family: "Oswald", sans-serif;
    font-weight: 700;
    font-size: 56px;
    fill: var(--panel-white);
  }
  .quote {
    font-family: "Poppins", sans-serif;
    font-weight: 600;
    font-size: 19px;
    fill: var(--ink);
  }
</style>
</head>
<body>
<main class="ad-set">

  <!-- Ad 1 -->
  <svg class="ad-post" viewBox="0 0 560 560" xmlns="http://www.w3.org/2000/svg">
    <defs>
      <linearGradient id="a1s1" x1="0" y1="0" x2="0.3" y2="1"><stop offset="0" stop-color="var(--slice1-top)"/><stop offset="1" stop-color="var(--slice1-low)"/></linearGradient>
      <linearGradient id="a1s2" x1="0" y1="0" x2="0.3" y2="1"><stop offset="0" stop-color="var(--slice2-top)"/><stop offset="1" stop-color="var(--slice2-low)"/></linearGradient>
      <linearGradient id="a1s3" x1="0" y1="0" x2="0.3" y2="1"><stop offset="0" stop-color="var(--slice3-top)"/><stop offset="1" stop-color="var(--slice3-low)"/></linearGradient>
      <linearGradient id="a1s4" x1="0" y1="0" x2="0.3" y2="1"><stop offset="0" stop-color="var(--slice4-top)"/><stop offset="1" stop-color="var(--slice4-low)"/></linearGradient>
      <linearGradient id="a1s5" x1="0" y1="0" x2="0.3" y2="1"><stop offset="0" stop-color="var(--slice5-top)"/><stop offset="1" stop-color="var(--slice5-low)"/></linearGradient>
      <linearGradient id="a1band" x1="0" y1="0" x2="1" y2="0"><stop offset="0" stop-color="var(--band-blue)"/><stop offset="1" stop-color="var(--band-violet)"/></linearGradient>
      <radialGradient id="a1shade" cx="0.5" cy="0.45" r="0.75"><stop offset="0.55" stop-color="#000" stop-opacity="0"/><stop offset="1" stop-color="#000" stop-opacity="0.35"/></radialGradient>
      <filter id="a1glow" x="-50%" y="-10%" width="200%" height="120%">
        <feGaussianBlur stdDeviation="3" result="b"/>
        <feMerge><feMergeNode in="b"/><feMergeNode in="b"/><feMergeNode in="SourceGraphic"/></feMerge>
      </filter>
    </defs>
    <g class="photo-collage">
      <polygon points="0,0 123,0 42,382 0,382" fill="url(#a1s1)" role="img" aria-label="Woman in a white tank top lifting a dumbbell overhead"/>
      <polygon points="123,0 255,0 179,382 42,382" fill="url(#a1s2)" role="img" aria-label="Smiling woman with pink hair doing a lunge"/>
      <polygon points="255,0 384,0 308,382 179,382" fill="url(#a1s3)" role="img" aria-label="Woman in a navy top doing a split squat"/>
      <polygon points="384,0 516,0 441,382 308,382" fill="url(#a1s4)" role="img" aria-label="Blonde woman holding a hex dumbbell in a squat"/>
      <polygon points="516,0 560,0 560,382 441,382" fill="url(#a1s5)" role="img" aria-label="Woman in a dark shirt pressing a weight overhead"/>
      <rect width="560" height="382" fill="url(#a1shade)"/>
    </g>
    <g class="split-lines" stroke="var(--glow)" stroke-width="2.5" filter="url(#a1glow)">
      <line x1="123" y1="0" x2="42" y2="382"/>
      <line x1="255" y1="0" x2="179" y2="382"/>
      <line x1="384" y1="0" x2="308" y2="382"/>
      <line x1="516" y1="0" x2="441" y2="382"/>
    </g>
    <rect class="color-band" y="382" width="560" height="178" fill="url(#a1band)"/>
    <polygon class="news-banner" points="39,348 423,348 410,416 25,416" fill="var(--news-red)"/>
    <text class="headline" x="45" y="405" textLength="338" lengthAdjust="spacingAndGlyphs" transform="skewX(-8)" transform-origin="45 405">BREAKING NEWS</text>
    <polygon class="panel-shadow" points="67,420 528,420 507,523 43,523" fill="#1a0a7a" opacity="0.6"/>
    <polygon class="quote-panel" points="63,412 523,412 502,514 39,514" fill="var(--panel-white)"/>
    <text class="quote" text-anchor="middle">
      <tspan x="279" y="452">Finally! Ridgecrest Gets the Gym That</tspan>
      <tspan x="279" y="475">Actually Delivers Results</tspan>
      <tspan x="279" y="497">(and It's Fun!)</tspan>
    </text>
  </svg>

  <!-- Ad 2 -->
  <svg class="ad-post" viewBox="0 0 560 560" xmlns="http://www.w3.org/2000/svg">
    <defs>
      <linearGradient id="a2s1" x1="0" y1="0" x2="0.3" y2="1"><stop offset="0" stop-color="var(--slice1-top)"/><stop offset="1" stop-color="var(--slice1-low)"/></linearGradient>
      <linearGradient id="a2s2" x1="0" y1="0" x2="0.3" y2="1"><stop offset="0" stop-color="var(--slice2-top)"/><stop offset="1" stop-color="var(--slice2-low)"/></linearGradient>
      <linearGradient id="a2s3" x1="0" y1="0" x2="0.3" y2="1"><stop offset="0" stop-color="var(--slice3-top)"/><stop offset="1" stop-color="var(--slice3-low)"/></linearGradient>
      <linearGradient id="a2s4" x1="0" y1="0" x2="0.3" y2="1"><stop offset="0" stop-color="var(--slice4-top)"/><stop offset="1" stop-color="var(--slice4-low)"/></linearGradient>
      <linearGradient id="a2s5" x1="0" y1="0" x2="0.3" y2="1"><stop offset="0" stop-color="var(--slice5-top)"/><stop offset="1" stop-color="var(--slice5-low)"/></linearGradient>
      <linearGradient id="a2band" x1="0" y1="0" x2="1" y2="0"><stop offset="0" stop-color="var(--band-blue)"/><stop offset="1" stop-color="var(--band-violet)"/></linearGradient>
      <radialGradient id="a2shade" cx="0.5" cy="0.45" r="0.75"><stop offset="0.55" stop-color="#000" stop-opacity="0"/><stop offset="1" stop-color="#000" stop-opacity="0.35"/></radialGradient>
      <filter id="a2glow" x="-50%" y="-10%" width="200%" height="120%">
        <feGaussianBlur stdDeviation="3" result="b"/>
        <feMerge><feMergeNode in="b"/><feMergeNode in="b"/><feMergeNode in="SourceGraphic"/></feMerge>
      </filter>
    </defs>
    <g class="photo-collage">
      <polygon points="0,0 123,0 42,382 0,382" fill="url(#a2s1)" role="img" aria-label="Woman in a white tank top lifting a dumbbell overhead"/>
      <polygon points="123,0 255,0 179,382 42,382" fill="url(#a2s2)" role="img" aria-label="Smiling woman with pink hair doing a lunge"/>
      <polygon points="255,0 384,0 308,382 179,382" fill="url(#a2s3)" role="img" aria-label="Woman in a navy top doing a split squat"/>
      <polygon points="384,0 516,0 441,382 308,382" fill="url(#a2s4)" role="img" aria-label="Blonde woman holding a hex dumbbell in a squat"/>
      <polygon points="516,0 560,0 560,382 441,382" fill="url(#a2s5)" role="img" aria-label="Woman in a dark shirt pressing a weight overhead"/>
      <rect width="560" height="382" fill="url(#a2shade)"/>
    </g>
    <g class="split-lines" stroke="var(--glow)" stroke-width="2.5" filter="url(#a2glow)">
      <line x1="123" y1="0" x2="42" y2="382"/>
      <line x1="255" y1="0" x2="179" y2="382"/>
      <line x1="384" y1="0" x2="308" y2="382"/>
      <line x1="516" y1="0" x2="441" y2="382"/>
    </g>
    <rect class="color-band" y="382" width="560" height="178" fill="url(#a2band)"/>
    <polygon class="news-banner" points="39,348 423,348 410,416 25,416" fill="var(--news-red)"/>
    <text class="headline" x="45" y="405" textLength="338" lengthAdjust="spacingAndGlyphs" transform="skewX(-8)" transform-origin="45 405">BREAKING NEWS</text>
    <polygon class="panel-shadow" points="67,420 528,420 507,523 43,523" fill="#1a0a7a" opacity="0.6"/>
    <polygon class="quote-panel" points="63,412 523,412 502,514 39,514" fill="var(--panel-white)"/>
    <text class="quote" text-anchor="middle">
      <tspan x="279" y="458">Ridgecrest Residents Ditch Boring Workouts</tspan>
      <tspan x="279" y="481">for This Life-Changing Fitness Experience</tspan>
    </text>
  </svg>

</main>
</body>
</html>
```